Business card design needed

Chasing a very simplistic modern design with a logo incorporating "TRV".
I'm starting a plumbing business.
I do water, sanitary and drainage plumbing that will cover residential, commercial, rental, rural, excavation, new housing and all maintanence requirements.

Industry/Entity Type

Business

Contact Information for Business Card

TRV PLUMBING SERVICES
DEAN HOLLOWBY - LICENSED PLUMBER
PHONE: 0481926574
E-MAIL: hollodt7@wirelane.com
NORTHERN SUBURBS

Requirements
Must have
• lower case email address

```html
<!DOCTYPE html>
<html lang="en">
<head>
<meta charset="utf-8">
<title>TRV Plumbing Services – Business Card</title>
<link rel="stylesheet" href="https://fonts.googleapis.com/css2?family=Didact+Gothic&display=swap">
<style>
  :root {
    --card-white: #ffffff;
    --band-grey: #6d6e71;
    --ink-dark: #231f20;
    --ink-soft: #808285;
    --text-light: #ffffff;
    --text-muted: #b3b4b6;
    --type: "Didact Gothic", "Century Gothic", sans-serif;
  }
  html, body {
    margin: 0;
    padding: 0;
    overflow: hidden;
    background: var(--card-white);
  }
  .card {
    position: relative;
    width: 693px;
    height: 1200px;
    overflow: hidden;
    font-family: var(--type);
    font-variant: small-caps;
    background: var(--card-white);
  }
  .brand {
    position: absolute;
    left: 0;
    top: 0;
    width: 693px;
    height: 543px;
    background: var(--card-white);
  }
  .brand-name {
    position: absolute;
    left: 62px;
    top: 330px;
    margin: 0;
    font-size: 96px;
    line-height: 1;
    font-weight: 400;
    letter-spacing: 2px;
    color: var(--ink-dark);
    font-variant: normal;
  }
  .brand-tagline {
    position: absolute;
    left: 65px;
    top: 424px;
    margin: 0;
    font-size: 27px;
    line-height: 1;
    letter-spacing: 1px;
    color: var(--ink-dark);
  }
  .contact-band {
    position: absolute;
    left: 0;
    top: 543px;
    width: 693px;
    height: 657px;
    background: var(--band-grey);
  }
  .contact-band p {
    position: absolute;
    left: 35px;
    margin: 0;
    line-height: 1;
    white-space: nowrap;
    letter-spacing: 1px;
  }
  .holder-name {
    top: 124px;
    font-size: 42px;
    color: var(--text-light);
  }
  .holder-role {
    top: 167px;
    font-size: 42px;
    color: var(--text-muted);
  }
  .phone {
    top: 300px;
    font-size: 33px;
    color: var(--text-light);
  }
  .email {
    top: 344px;
    font-size: 33px;
    color: var(--text-light);
  }
  .area {
    top: 451px;
    font-size: 33px;
    color: var(--text-light);
  }
</style>
</head>
<body>
  <div class="card">
    <header class="brand">
      <h1 class="brand-name">TRV</h1>
      <p class="brand-tagline">Plumbing Services</p>
    </header>
    <section class="contact-band">
      <p class="holder-name">Dean Hollowby</p>
      <p class="holder-role">Licensed Plumber</p>
      <p class="phone">Phone: 0481926574</p>
      <p class="email">E-Mail: hollodt7@wirelane.com</p>
      <p class="area">Northern suburbs</p>
    </section>
  </div>
</body>
</html>
```